Holistic Psychologist needs contemporary business card

I am a psychologist working with adult clients face to face and online. The card needs to work for clients and also referring doctors and medical professionals. It needs to look warm, safe and trustable for clients, but clean and professional enough for doctors. Sometimes I also work in a corporate context.

I am holistic in my approach (mind-body-spirit) so anything conveying connection or integration or wholeness would be good. But again, clean and contemporary please. It can have a little bit of personality.
New logo uploaded.

Probably warm tones and plenty white space to write on one side.

My web pages:
http://mkcounsel.com.au
https://www.facebook.com/MarionKellerCounselling?ref=hl
Updates

Hi Designers .. I have decided I do need a new logo before finalising a design for the business cards.  I hope to have this available in 4 days from now.

Kindly,

Marion

New logo now posted, same brief.  Balance of masculine and feminine elements, plenty of white space on one side please.

Keen to see some card designs, thank-you.

Target Market(s)

Audience 1 - Males and females aged 25 years + seeking counselling or coaching. Audience 2 - doctors and health professionals who refer clients.

Industry/Entity Type

Medical

Contact Information for Business Card

Logo

Marion Keller
Registered Psychologist

M: 0491 582 034
www.mkcounsel.com.au
marion@mkcounsel.com.au
Little blue Facebook icon, with "marion keller counselling" printed near it.

Font styles to use
Sans Serif

Requirements
Nice to have
• You might want to play with the words "wholly you"
Should not have
• Nothing cutesy or too literal

```html
<!DOCTYPE html>
<html lang="en">
<head>
<meta charset="utf-8">
<title>Marion Keller Counselling – Business Card</title>
<link rel="stylesheet" href="https://fonts.googleapis.com/css2?family=Bebas+Neue&family=Quicksand:wght@500;600&display=swap">
<style>
  :root {
    --backdrop: #e9d9c6;
    --gold-light: #fff3a0;
    --gold-mid: #fde047;
    --gold-deep: #f7b90f;
    --brand-red: #e31e24;
    --ink: #2b2b2b;
    --white: #ffffff;
    --rule: #b9b9b9;
    --faint-peach: #f8d3c4;
    --social-blue: #3b5998;
  }
  * { box-sizing: border-box; margin: 0; padding: 0; }
  html, body { width: 932px; height: 1200px; overflow: hidden; }
  body {
    position: relative;
    background: var(--backdrop);
    font-family: "Quicksand", sans-serif;
  }
  .card {
    position: absolute;
    left: 62px;
    width: 808px;
    overflow: hidden;
    box-shadow: 0 6px 14px rgba(80, 50, 20, 0.35);
  }
  .card--front {
    top: 62px;
    height: 490px;
    border-radius: 52px 0 52px 0;
    background: radial-gradient(ellipse 620px 520px at 230px 70px, var(--gold-light) 0%, var(--gold-mid) 45%, var(--gold-deep) 100%);
  }
  .card--back {
    top: 650px;
    height: 488px;
    border-radius: 0 52px 0 52px;
    background: var(--white);
  }
  .brand {
    position: absolute;
    display: flex;
    align-items: center;
    gap: 14px;
  }
  .card--front .brand { left: 46px; top: 62px; }
  .card--back .brand { left: 54px; top: 58px; }
  .brand__dot {
    width: 40px; height: 40px;
    border-radius: 50%;
    background: var(--brand-red);
  }
  .brand__name {
    font-weight: 600;
    font-size: 36px;
    line-height: 1;
    color: var(--brand-red);
  }
  .holder {
    position: absolute;
    left: 50px; top: 188px;
    font-family: "Bebas Neue", sans-serif;
    color: var(--ink);
    text-shadow: 1px 2px 2px rgba(0, 0, 0, 0.25);
  }
  .holder__name { font-size: 46px; line-height: 1; letter-spacing: 0.5px; }
  .holder__title {
    margin-top: 14px;
    font-size: 25px;
    line-height: 1;
    color: var(--white);
    text-shadow: 1px 1px 2px rgba(0, 0, 0, 0.35);
  }
  .contacts {
    position: absolute;
    left: 46px; top: 334px;
    list-style: none;
  }
  .contacts li {
    display: flex;
    align-items: center;
    gap: 12px;
    height: 32px;
    font-size: 23px;
    font-weight: 500;
    color: var(--ink);
  }
  .contacts__icon {
    width: 22px; height: 22px;
    display: flex; align-items: center; justify-content: center;
    background: var(--brand-red);
    color: var(--white);
    font-size: 15px;
    font-weight: 600;
    border-radius: 2px;
  }
  .contacts__icon--social { background: var(--social-blue); }
  .accent {
    position: absolute;
    right: -60px; top: 120px;
    width: 360px; height: 360px;
  }
  .accent__tagline {
    font-family: "Quicksand", sans-serif;
    font-size: 26px;
    font-weight: 500;
    letter-spacing: 2px;
  }
  .rules {
    position: absolute;
    left: 53px; top: 142px;
    width: 700px;
  }
  .rules span {
    display: block;
    height: 50px;
    border-bottom: 2px dotted var(--rule);
  }
</style>
</head>
<body>

<section class="card card--front">
  <svg class="accent" viewBox="0 0 360 360" aria-hidden="true">
    <circle cx="180" cy="180" r="170" fill="var(--brand-red)"/>
    <text class="accent__tagline" x="150" y="290" text-anchor="middle" fill="var(--white)">wholly you</text>
  </svg>

  <div class="brand">
    <span class="brand__dot"></span>
    <span class="brand__name">Marion Keller Counselling</span>
  </div>

  <div class="holder">
    <h1 class="holder__name">Marion Keller</h1>
    <p class="holder__title">Registered Psychologist</p>
  </div>

  <ul class="contacts">
    <li><span class="contacts__icon">m</span>0491 582 034</li>
    <li><span class="contacts__icon">e</span>marion@mkcounsel.com.au</li>
    <li><span class="contacts__icon contacts__icon--social"></span>marion keller counselling</li>
    <li><span class="contacts__icon">w</span>www.mkcounsel.com.au</li>
  </ul>
</section>

<section class="card card--back">
  <svg class="accent" viewBox="0 0 360 360" aria-hidden="true">
    <circle cx="180" cy="180" r="170" fill="var(--faint-peach)"/>
    <text class="accent__tagline" x="150" y="290" text-anchor="middle" fill="var(--white)">wholly you</text>
  </svg>

  <div class="brand">
    <span class="brand__dot"></span>
    <span class="brand__name">Marion Keller Counselling</span>
  </div>

  <div class="rules">
    <span></span><span></span><span></span><span></span><span></span><span></span>
  </div>
</section>

</body>
</html>
```